Roll Up Design Velmora

We are a beauty company and we need stunning design for our general roll-up banner that we gonna place just next to the main gate of mall that we are located in. The most important for us is the quality, accuracy and the unity of poster. It has to be super elegant, engaging and beautiful. Has to match our service standards (high). Colors do not matter as long as the overall look is exciting.
Examples and our logo are attached
Updates
Reason: We need more designs (more creativity, more quality, colurs and proportions).
Target Market(s)
Middle class ladies, students, business women
Industry/Entity Type
It Company
Colors
Designer to choose colors to be used in the design.
Look and feel
Each slider illustrates characteristics of the customer's brand and the style your logo design should communicate.

```html
<!DOCTYPE html>
<html lang="en">
<head>
<meta charset="utf-8">
<title>Velmora Gözəllik – Roll-up Banner</title>
<link rel="stylesheet" href="https://fonts.googleapis.com/css2?family=Marcellus+SC&family=Montserrat:wght@400&display=swap">
<style>
  :root {
    --paper: #ffffff;
    --edge: #d9d9d9;
    --brand-grey: #8f8f8f;
    --rule: #b5b5b5;
    --service: #6e6e6e;
    --contact: #7a7a7a;
    --tone-light: #f4e4d9;
    --tone-mid: #ead0bf;
    --tone-deep: #dfbfa9;
  }
  html, body {
    margin: 0;
    padding: 0;
    width: 1200px;
    height: 3000px;
    overflow: hidden;
    background: var(--paper);
  }
  .banner {
    position: relative;
    width: 1200px;
    height: 3000px;
    box-sizing: border-box;
    border: 2px solid var(--edge);
    background: var(--paper);
    font-family: "Marcellus SC", "Times New Roman", serif;
  }
  .brand {
    position: absolute;
    top: 196px;
    left: 0;
    width: 100%;
    text-align: center;
  }
  .brand-name {
    margin: 0;
    font-family: "Marcellus SC", serif;
    font-weight: 400;
    font-size: 150px;
    line-height: 1;
    letter-spacing: 4px;
    color: var(--brand-grey);
  }
  .brand-rule {
    width: 472px;
    height: 0;
    border-top: 3px solid var(--rule);
    margin: 26px auto 0;
  }
  .brand-sub {
    margin: 18px 0 0;
    font-family: "Montserrat", Arial, sans-serif;
    font-weight: 400;
    font-size: 54px;
    letter-spacing: 5px;
    color: var(--brand-grey);
  }
  .services {
    position: absolute;
    top: 587px;
    left: 0;
    width: 100%;
    margin: 0;
    padding: 0;
    list-style: none;
    text-align: center;
  }
  .services li {
    font-size: 31px;
    line-height: 56.2px;
    letter-spacing: 2px;
    text-transform: uppercase;
    color: var(--service);
  }
  .portrait {
    position: absolute;
    top: 1537px;
    left: 25px;
    width: 1150px;
    height: 1100px;
    background: linear-gradient(180deg, var(--tone-light) 0%, var(--tone-mid) 60%, var(--tone-deep) 100%);
  }
  .contacts {
    position: absolute;
    top: 2708px;
    left: 0;
    width: 100%;
    text-align: center;
    color: var(--contact);
    text-transform: uppercase;
  }
  .contacts p {
    margin: 0;
    line-height: 55px;
  }
  .contact-web {
    font-size: 38px;
    letter-spacing: 3px;
  }
  .contact-phone {
    font-size: 46px;
    letter-spacing: 3px;
  }
</style>
</head>
<body>
  <main class="banner">
    <header class="brand">
      <h1 class="brand-name">VELMORA</h1>
      <div class="brand-rule"></div>
      <p class="brand-sub">GÖZƏLLİK</p>
    </header>

    <ul class="services">
      <li>Laser Hair Removal</li>
      <li>Skin Brightening</li>
      <li>Eyebrowns</li>
      <li>Eyelash Tinting</li>
      <li>Aromatherapy</li>
      <li>Hot Stone Massage</li>
      <li>Hair Services</li>
      <li>Laser Hair Removal</li>
      <li>Skin Brightening</li>
      <li>Eyebrowns</li>
      <li>Eyelash Tinting</li>
      <li>Aromatherapy</li>
      <li>Hot Stone Massage</li>
      <li>Hair Services</li>
    </ul>

    <div class="portrait" role="img" aria-label="Beauty photograph: blonde woman with bare shoulders holding ice cubes against her jawline on a white background"></div>

    <footer class="contacts">
      <p class="contact-web">www.velmoragozellik.com</p>
      <p class="contact-web">office@velmoragozellik.com</p>
      <p class="contact-phone">(012) 418 2790 · (051) 736 2790</p>
      <p class="contact-phone">(055) 825 2790 &nbsp;· (070) 293 2790</p>
    </footer>
  </main>
</body>
</html>
```